Vellmora- plumbing service flyer

Hello,
We would like to create flyer for our plumbing company Vellmora
- we have 2 web domains
vellmora-example.hr ( official)
preuredbastanova-example.hr ( for bathroom renovation)

- we would like to create a similar Z-fold flyer ( from A4 paper) for our services
- We are sending images used on our websites. Of Course, it is allowed to put some of their own. Depending on design
- sending word with text which should go on each page. Text can be modified but in the sense of a page. The massage on a page should be as in word.
What is important to us:
- to stay in blue color
- It should be 1 page when fully open. So it looks like the complete page of information
- first/front page should be with our logo and phone number. more focus on emergency plumbing.
- back page should be about bathroom remodeling. Not necessary but would be received more points
- please don't use images of regular plumbers from Pixelgrove and similar. we don't want to use this stock's regular images as all others.

Target Market(s)

Bathroom remodeling and emergency plumbing

Industry/Entity Type

Construction-Plumbing

Colors
0054AA
0677BA
7BADD7
CADEEF
E8F1F8

Requirements
Must have
• Logo

```html
<!DOCTYPE html>
<html lang="en">
<head>
<meta charset="utf-8">
<title>Vellmora – Plumbing Service Z-fold Flyer</title>
<link href="https://fonts.googleapis.com/css2?family=Oswald:wght@500;600;700&family=Open+Sans:wght@400;600&display=swap" rel="stylesheet">
<style>
:root{
  --navy:#0f2a5c;
  --navy-deep:#0b1f47;
  --blue:#1d4f96;
  --blue-bright:#0677BA;
  --blue-light:#7BADD7;
  --blue-pale:#CADEEF;
  --yellow:#f5b31c;
  --red:#e3101c;
  --white:#ffffff;
  --ink:#1a1a1a;
  --stage:#e4e4e4;
}
*{margin:0;padding:0;box-sizing:border-box}
html,body{width:1200px;height:3464px;overflow:hidden;background:var(--stage)}
body{position:relative;font-family:"Open Sans",Arial,sans-serif}
.spread{position:absolute;left:40px;width:1120px;height:792px;display:flex;box-shadow:0 4px 14px rgba(0,0,0,.18)}
.spread--outside{top:920px}
.spread--inside{top:1752px}
.panel{position:relative;width:373.33px;height:100%;overflow:hidden;display:flex;flex-direction:column}
.panel--yellow{background:var(--yellow)}
.panel--navy{background:var(--navy)}
.panel--blue{background:var(--blue)}
.photo{height:200px;background:linear-gradient(160deg,#c9c2b8,#8a7c70 55%,#3c4d6e);flex:none}
.photo--navy{background:linear-gradient(160deg,#d9d6d2,#7d8696 55%,#1e3564);height:225px}
.brand{font-family:"Oswald",sans-serif;font-weight:700;color:var(--blue-bright);text-transform:uppercase;text-align:center;letter-spacing:1px;line-height:1}
.brand--xl{font-size:62px}
.brand--l{font-size:58px}
.brand--light{color:var(--blue-light)}
.logo{display:flex;flex-direction:column;align-items:center;gap:10px;margin-top:28px}
.logo__mark{width:150px;height:150px;border-radius:50%;background:var(--blue-pale)}
.logo__name{font-family:"Oswald",sans-serif;font-weight:700;font-size:46px;color:var(--white);text-transform:uppercase;line-height:1.1}
.body{padding:0 22px;font-size:12px;color:var(--ink);line-height:1.3}
.body p{margin-top:8px}
.checks{list-style:none;padding:0 0 0 20px;margin-top:8px;width:262px;color:var(--navy)}
.checks li{font-family:"Oswald",sans-serif;font-weight:500;font-size:13px;color:var(--navy);display:flex;gap:7px;padding:4px 0;border-bottom:1px solid rgba(15,42,92,.25);line-height:1.15}
.checks li:last-child{border:0}
.checks svg{flex:none;margin-top:1px;color:var(--navy)}
.mascot{position:absolute;background:radial-gradient(circle at 50% 40%,#3f8fdd,#1b4f9c);border-radius:40% 40% 10% 10%}
.phone-band{position:absolute;left:0;right:0;height:50px;background:var(--red);display:flex;align-items:center;justify-content:center;gap:12px}
.phone-band span{font-family:"Oswald",sans-serif;font-weight:600;font-size:34px;color:var(--white);letter-spacing:.5px}
.spread--outside .phone-band{top:608px}
.spread--inside .phone-band{top:728px}
.foot{position:absolute;left:0;right:0;top:658px;bottom:0;display:flex;flex-direction:column;align-items:center;justify-content:center;text-align:center;font-family:"Oswald",sans-serif;font-weight:700;text-transform:uppercase;line-height:1.05}
.foot--yellow{color:var(--navy-deep)}
.foot--navy{background:var(--navy-deep)}
.foot__small{font-size:23px}
.foot__big{font-size:46px}
.foot__yellow{color:var(--yellow);font-size:42px}
.foot__cyan{color:#14a9e6;font-size:34px}
.contacts{font-family:"Open Sans",Arial,sans-serif;text-transform:none;font-size:15px;color:var(--white);line-height:1.75;text-align:center;font-weight:600}
.dots{display:flex;gap:8px;justify-content:center;margin-bottom:4px}
.dots i{width:18px;height:18px;border-radius:50%;background:var(--yellow);display:block}
.pill{align-self:center;font-family:"Oswald",sans-serif;font-weight:600;text-transform:uppercase;border-radius:20px;padding:2px 18px}
.pill--red{background:var(--red);color:var(--white);font-size:22px;margin-top:12px}
.pill--yellow{background:var(--yellow);color:var(--navy);font-size:24px;margin-top:18px}
.subhead{font-family:"Oswald",sans-serif;font-weight:600;color:var(--yellow);font-size:20px;text-align:center;margin-top:8px;text-transform:uppercase}
.svc-list{list-style:none;padding:10px 30px 0}
.svc-list li{color:var(--white);font-size:15px;display:flex;align-items:center;gap:14px;padding:6px 0;border-bottom:1px solid rgba(245,179,28,.45)}
.svc-list li:last-child{border:0}
.svc-list svg{color:var(--yellow);flex:none}
.callout{position:absolute;left:40px;right:40px;top:526px;height:82px;background:var(--blue-bright);border-radius:14px 14px 0 0;color:var(--white);font-family:"Oswald",sans-serif;font-weight:500;font-size:19px;text-align:center;display:flex;align-items:center;justify-content:center;line-height:1.2;padding:0 10px}
.services{list-style:none;padding:14px 22px 0}
.services li{display:flex;align-items:center;gap:16px;padding:8px 0;font-family:"Oswald",sans-serif;font-weight:500;font-size:28px;color:var(--white)}
.ico{width:44px;height:44px;border-radius:50%;background:var(--blue-pale);flex:none;display:flex;align-items:center;justify-content:center;color:var(--blue)}
.steps-title{font-family:"Oswald",sans-serif;font-weight:600;color:var(--yellow);font-size:30px;text-align:center;margin-top:4px;line-height:1.3}
.steps{list-style:none;padding:4px 30px 0;font-family:"Oswald",sans-serif;font-weight:500;font-size:22px;color:var(--white);line-height:1.3}
.contact-box{margin:12px 38px 0;background:var(--blue-bright);border-radius:14px;padding:8px 0 6px}
.contact-box .contacts{font-size:14px;line-height:1.65}
.check-box{margin:20px 22px 0;background:var(--navy-deep);border-radius:0 0 18px 18px;padding:20px 10px 16px;text-align:center}
.check-box h3{font-family:"Oswald",sans-serif;font-weight:600;color:var(--white);font-size:25px;line-height:1.2;text-transform:uppercase;margin-top:10px}
.numbered{list-style:none;padding:14px 28px 0;font-size:15px;color:var(--ink)}
.numbered li{padding:6px 0;border-bottom:1px solid rgba(15,42,92,.3);line-height:1.3}
.numbered li:last-child{border:0}
.note{font-family:"Oswald",sans-serif;font-weight:500;color:var(--navy-deep);font-size:20px;text-align:center;padding:12px 24px 0;line-height:1.2}
.reno{list-style:none;padding:14px 30px 0}
.reno li{display:flex;align-items:center;gap:18px;padding:5px 0;border-bottom:1px solid rgba(255,255,255,.3);font-family:"Oswald",sans-serif;font-weight:500;font-size:19px;color:var(--white)}
.reno li:last-child{border:0}
.reno b{width:36px;height:36px;border-radius:50%;background:var(--white);border:3px solid var(--yellow);color:var(--navy);display:flex;align-items:center;justify-content:center;font-size:16px;flex:none}
.reno-note{color:var(--white);font-size:12.5px;text-align:center;padding:12px 26px 0;line-height:1.35}
</style>
</head>
<body>

<svg width="0" height="0" style="position:absolute">
  <defs>
    <symbol id="phone" viewBox="0 0 36 36"><circle cx="18" cy="18" r="17" fill="#fff"/><path d="M11 9c1-1 3-1 4 0l2 3c.6 1 .3 2-.5 2.8l-1 1c1 2.3 2.8 4.1 5 5l1-1c.8-.8 1.9-1 2.8-.5l3 2c1 .7 1 2.3 0 3.3-2 2-5 2.2-8 .2-3.5-2.3-6.6-5.4-8.8-8.9C8.7 14.1 9 11 11 9z" fill="#e3101c"/></symbol>
    <symbol id="tick" viewBox="0 0 14 14"><rect x="1" y="1" width="12" height="12" rx="2" fill="none" stroke="currentColor" stroke-width="1.5"/><path d="M3.5 7l2.5 2.5 5-5.5" fill="none" stroke="currentColor" stroke-width="1.8"/></symbol>
    <symbol id="wrench" viewBox="0 0 20 20"><path d="M13 2a5 5 0 0 0-4.6 6.9L2.5 14.8a1.8 1.8 0 0 0 2.6 2.6l5.9-5.9A5 5 0 0 0 17.8 7l-3 3-2.4-.6-.6-2.4 3-3A5 5 0 0 0 13 2z" fill="currentColor"/></symbol>
  </defs>
</svg>

<section class="spread spread--outside">
  <div class="panel panel--yellow">
    <div class="photo" role="img" aria-label="Photo of a plumber repairing pipework under a sink"></div>
    <h2 class="brand brand--xl" style="margin-top:10px">Vellmora</h2>
    <div class="body">
      <p>Do you need a plumber for bathroom renovation? Did your pipe burst or have some clogging in pipes? The neighbor's has ceiling leak?</p>
      <p>We offer plumbing services in the area of the City of Zagreb and its surroundings. Some of the common plumbing services include:</p>
    </div>
    <ul class="checks">
      <li><svg width="14" height="14"><use href="#tick"/></svg>Installation of new plumbing systems</li>
      <li><svg width="14" height="14"><use href="#tick"/></svg>Repair of leaking pipes, faucets, and fixtures</li>
      <li><svg width="14" height="14"><use href="#tick"/></svg>Drain cleaning and unclogging</li>
      <li><svg width="14" height="14"><use href="#tick"/></svg>Sewer line repair and replacement</li>
      <li><svg width="14" height="14"><use href="#tick"/></svg>Bathroom and kitchen plumbing installation and repair</li>
    </ul>
    <div class="mascot" style="left:280px;top:460px;width:90px;height:148px" role="img" aria-label="Illustrated masked plumber mascot holding a pipe wrench"></div>
    <div class="phone-band"><svg width="36" height="36"><use href="#phone"/></svg><span>+385 91 555 0142</span></div>
    <div class="foot foot--yellow"><span class="foot__small">Reliability, speed, accessibility</span><span class="foot__big">Your Vellmora</span></div>
  </div>

  <div class="panel panel--navy">
    <h2 class="brand brand--l brand--light" style="margin-top:44px">Vellmora</h2>
    <div class="pill pill--red">Emergency plumbing</div>
    <div class="subhead">Emergency services</div>
    <ul class="svc-list">
      <li><svg width="18" height="18"><use href="#wrench"/></svg>Mechanical drain cleaning</li>
      <li><svg width="18" height="18"><use href="#wrench"/></svg>Water jet pipe cleaning</li>
      <li><svg width="18" height="18"><use href="#wrench"/></svg>Leak detections</li>
      <li><svg width="18" height="18"><use href="#wrench"/></svg>Pipe inspection with camera</li>
      <li><svg width="18" height="18"><use href="#wrench"/></svg>Thermal imaging of leakes</li>
      <li><svg width="18" height="18"><use href="#wrench"/></svg>Main pipe check up</li>
      <li><svg width="18" height="18"><use href="#wrench"/></svg>Valve change</li>
      <li><svg width="18" height="18"><use href="#wrench"/></svg>Change of sink siphon</li>
    </ul>
    <div class="callout">Vellmora team will help you to manage all the plumbing crises.</div>
    <div class="phone-band"><svg width="36" height="36"><use href="#phone"/></svg><span>+385 91 555 0142</span></div>
    <div class="foot foot--navy"><span class="foot__yellow">Fast and reliable</span><span class="foot__cyan">Contact us daily 24/7</span></div>
  </div>

  <div class="panel panel--blue">
    <div class="logo"><div class="logo__mark"></div><div class="logo__name">Vellmora</div></div>
    <div class="pill pill--yellow">Our services</div>
    <ul class="services">
      <li><span class="ico"><svg width="22" height="22"><use href="#wrench"/></svg></span>Bathroom remodeling</li>
      <li><span class="ico"><svg width="22" height="22"><use href="#wrench"/></svg></span>Emergency plumbing</li>
      <li><span class="ico"><svg width="22" height="22"><use href="#wrench"/></svg></span>Plumbing</li>
      <li><span class="ico"><svg width="22" height="22"><use href="#wrench"/></svg></span>Lek detection</li>
    </ul>
    <div class="phone-band"><svg width="36" height="36"><use href="#phone"/></svg><span>+385 91 555 0142</span></div>
    <div class="foot"><div class="dots"><i></i><i></i><i></i></div>
      <div class="contacts">info@vellmora-example.hr<br>www.vellmora-example.hr<br>www.preuredbastanova-example.hr</div></div>
  </div>
</section>

<section class="spread spread--inside">
  <div class="panel panel--navy">
    <div class="photo photo--navy" role="img" aria-label="Photo of a plumber checking pipes under a washbasin"></div>
    <h2 class="brand brand--xl" style="margin-top:8px">Vellmora</h2>
    <div class="steps-title">PLUMBING STEPS</div>
    <ol class="steps">
      <li>1. Planning faze</li><li>2. Demolition</li><li>3. Plumbing faze</li><li>4. Electric work</li>
      <li>5. Ceramic work</li><li>6. Final sanitary installation</li><li>7. Final cleaning</li>
    </ol>
    <div class="contact-box"><div class="dots"><i></i><i></i><i></i></div>
      <div class="contacts">info@vellmora-example.hr<br>www.vellmora-example.hr<br>www.preuredbastanova-example.hr</div></div>
    <div class="phone-band"><svg width="36" height="36"><use href="#phone"/></svg><span>+385 91 555 0142</span></div>
  </div>

  <div class="panel panel--yellow">
    <div class="check-box">
      <h2 class="brand brand--l">Vellmora</h2>
      <h3>What to check before inastallation and putting tiles on walls.</h3>
    </div>
    <ol class="numbered">
      <li>1. Decide on type of pipes: PEX, PPR, Inox</li>
      <li>2. Inspect pipes with camera to check is pipe fall ok</li>
      <li>3. Test water pipes with test pump</li>
      <li>4. Take images of each wall with install pipes on it before closing.</li>
    </ol>
    <p class="note">This steps will help you to be sure that installations are ok before closing</p>
    <div class="mascot" style="left:118px;top:545px;width:140px;height:183px" role="img" aria-label="Illustrated masked plumber mascot giving a thumbs up"></div>
    <div class="phone-band"><svg width="36" height="36"><use href="#phone"/></svg><span>+385 91 555 0142</span></div>
  </div>

  <div class="panel panel--blue">
    <div class="logo" style="margin-top:20px"><div class="logo__mark" style="width:140px;height:140px"></div><div class="logo__name">Vellmora</div></div>
    <div class="pill pill--yellow" style="font-size:20px;margin-top:14px">Steps for renovating a bathroom</div>
    <ol class="reno">
      <li><b>01</b>Plan your budget</li>
      <li><b>02</b>Plan your design</li>
      <li><b>03</b>Hire a proffesionals</li>
      <li><b>04</b>Decide about sanitary ware</li>
      <li><b>05</b>Choose tile and paint</li>
      <li><b>06</b>Install bathroom accessories</li>
      <li><b>07</b>Clean up</li>
    </ol>
    <p class="reno-note">By following these steps, you can successfully renovate your bathroom and create a space that meets your needs and style preferences.</p>
    <div class="phone-band"><svg width="36" height="36"><use href="#phone"/></svg><span>+385 91 555 0142</span></div>
  </div>
</section>

</body>
</html>
```